“The Future” Spring Fair Poster

We are putting together a school and community fair. We need a poster designed to advertise the event and give some important information to would be attendees. We’d like the poster graphics to evoke a minimalistic and futuristic aesthetic, be bold, yet fun! We will printing the posters, so we will need for them to be at high resolution and ready to send to print.

Target Market(s)

Students, Parents, and Community members

Industry/Entity Type

School

Font styles to use
Sans Serif

Colors
33a6d7
fabb78
9d9d9d
ffffff
1b1b1b
33b8a4

Requirements
Must have
• The Future
• Birch & Harbor Spring Fair 2018
• Friday, May 18th
• 5:00-9:00pm
• Tickets Will Be Available at Select Pick up & Drop Off Times
• Come Enjoy a Futuristic Evening of Food, Music, Entertainment, & Fun!
Nice to have
• We’d love to see a bold and graphic poster with a futuristic feel!
• See the sample image below from previous event poster and additional images for mood and inspiration. Would love to see metallics (silver or metallic colors)

```html
<!DOCTYPE html>
<html lang="en">
<head>
<meta charset="utf-8">
<title>Birch &amp; Harbor Spring Fair 2018 – The Future</title>
<link rel="stylesheet" href="https://fonts.googleapis.com/css2?family=Open+Sans:wght@400;600&family=Montserrat:wght@900&display=swap">
<style>
  :root {
    --night: #050505;
    --ink: #1b1b1b;
    --white: #ffffff;
    --silver: #9d9d9d;
    --teal: #33b8a4;
    --aqua: #3fe6d6;
    --mint: #31d990;
    --sky: #33a6d7;
    --peach: #fabb78;
  }
  * { margin: 0; padding: 0; box-sizing: border-box; }
  html, body { width: 849px; height: 1200px; overflow: hidden; background: var(--night); }
  .poster {
    position: relative;
    width: 849px;
    height: 1200px;
    overflow: hidden;
    background: radial-gradient(ellipse at 50% 45%, var(--ink) 0%, var(--night) 70%);
    font-family: "Open Sans", Arial, sans-serif;
    color: var(--white);
  }
  .poster__art { position: absolute; inset: 0; }
  .glow { text-shadow: 0 0 8px rgba(255,255,255,.55), 0 0 2px rgba(255,255,255,.8); }
  .headline {
    position: absolute; left: 0; right: 0; top: 88px;
    text-align: center; font-size: 42px; font-weight: 400; letter-spacing: .2px;
  }
  .theme-title {
    position: absolute; left: 0; right: 0; top: 483px;
    text-align: center; font-family: "Montserrat", Arial, sans-serif;
    font-weight: 900; font-size: 64px; letter-spacing: -1px; line-height: 1;
  }
  .event-date {
    position: absolute; left: 0; right: 0; top: 902px;
    text-align: center; font-size: 40px; line-height: 1.2;
  }
  .event-time {
    position: absolute; left: 0; right: 0; top: 963px;
    text-align: center; font-size: 29px; line-height: 1.2;
  }
  .ticket-note {
    position: absolute; left: 0; right: 0; top: 1072px;
    text-align: center; font-size: 19px; line-height: 1.2;
  }
  .invite {
    position: absolute; left: 0; right: 0; top: 1131px;
    text-align: center; font-size: 20px; line-height: 1.2;
  }
</style>
</head>
<body>
<main class="poster">
  <svg class="poster__art" width="849" height="1200" viewBox="0 0 849 1200" xmlns="http://www.w3.org/2000/svg">
    <defs>
      <radialGradient id="shard-haze" cx="50%" cy="50%" r="50%">
        <stop offset="0%" stop-color="#6d6a3a" stop-opacity=".55"/>
        <stop offset="45%" stop-color="#2e6f7a" stop-opacity=".35"/>
        <stop offset="100%" stop-color="#1b1b1b" stop-opacity="0"/>
      </radialGradient>
      <linearGradient id="ring-metal" x1="0" y1="0" x2="1" y2="1">
        <stop offset="0%" stop-color="#f2f2f2"/>
        <stop offset="50%" stop-color="#9d9d9d"/>
        <stop offset="100%" stop-color="#d8d8d8"/>
      </linearGradient>
      <linearGradient id="core-fill" x1="0" y1="0" x2="0" y2="1">
        <stop offset="0%" stop-color="var(--aqua)"/>
        <stop offset="100%" stop-color="var(--mint)"/>
      </linearGradient>
    </defs>
    <g role="img" aria-label="Starfield with bursts of translucent coloured glass shards radiating around the ring">
      <ellipse cx="440" cy="520" rx="440" ry="380" fill="url(#shard-haze)"/>
    </g>
    <circle class="ring" cx="424" cy="518" r="297" fill="none" stroke="url(#ring-metal)" stroke-width="20"/>
    <circle class="ring-inner" cx="424" cy="518" r="287" fill="#0b0b0b" opacity=".55"/>
    <circle class="core" cx="424" cy="516" r="208" fill="url(#core-fill)"/>
  </svg>

  <h1 class="headline glow">Birch &amp; Harbor Spring Fair 2018</h1>
  <h2 class="theme-title">THE FUTURE</h2>
  <p class="event-date glow">Friday, May 18th</p>
  <p class="event-time glow">5:00-9:00pm</p>
  <p class="ticket-note glow">Tickets Will Be Available at Select Pick up &amp; Drop Off Times</p>
  <p class="invite glow">Come Enjoy a Futuristic Evening of Food, Music, Entertainment, &amp; Fun!</p>
</main>
</body>
</html>
```